Business Card 85x40mm - Freelance audio mixing / live event operator

I am a freelance audio operator working in live events. Mostly corporate events mixing sound for a range of entertainment, awards nights and functions. I need a new card to give to perspective clients.

The final design will convey bold professionalism with a general dark vibe. Looking for dark-ish background with some smatterings of colour added.

I have attatched my old BC for an idea of what I have liked in the past. Id like a more modern updated design (that circular design on the back is not my logo it is just a picture I found that resembled sound} . For an added element possibly a mixture of some playful colours in a way that resembles an audio wave form or sound.

I have attached a photo called "audio software" with some colourful squiggly lines; maybe incorporate elements of that into into design
Updates

Added extra $ to project Damn Pixel hives fees are unreasonable

Target Market(s)

Mostly corporate clients

Industry/Entity Type

Events

Contact Information for Business Card

Corwin Pellath
Sound | FOH | Monitors | Systems | Corporate

Digital Audio Mixing Specialist, Live Event Technical Professional,

corwinpellath@mailvexo.net, +61 402 918 357

Colors
ec1f27
ffc214
9bcb3c
6b449b

Requirements
Must have
• Dark theme
• 85x40mm dimensions
Nice to have
• some sort of imagery or design to reflect audio/sound

```html
<!DOCTYPE html>
<html lang="en">
<head>
<meta charset="utf-8">
<title>Corwin Pellath – Business Card</title>
<link rel="stylesheet" href="https://fonts.googleapis.com/css2?family=Lora:wght@400&display=swap">
<style>
  :root {
    --page-bg: #2a2622;
    --card-black: #050505;
    --card-dark: #1a1a1a;
    --ink-light: #f2f2f2;
    --red: #ec1f27;
    --yellow: #ffc214;
    --green: #9bcb3c;
    --purple: #6b449b;
    --orange: #f2701e;
    --cyan: #4fb3d4;
  }
  * { margin: 0; padding: 0; box-sizing: border-box; }
  html, body {
    width: 1189px; height: 1200px; overflow: hidden;
    background: var(--page-bg);
    font-family: "Lora", Georgia, serif;
  }
  .card {
    position: absolute; left: 170px; width: 852px; height: 400px;
    overflow: hidden;
    box-shadow: 0 6px 18px rgba(0,0,0,.5);
  }
  .card--front { top: 171px; background: var(--card-black); }
  .card--back  { top: 632px; background: var(--card-dark); }

  .waveform {
    position: absolute; inset: 0;
    background:
      linear-gradient(90deg, rgba(236,31,39,.85) 0%, rgba(242,112,30,.75) 20%, rgba(255,194,20,.85) 45%, rgba(155,203,60,.75) 65%, rgba(79,179,212,.8) 90%, rgba(79,179,212,.3) 100%);
    -webkit-mask-image: linear-gradient(180deg, transparent 0%, #000 30%, #000 70%, transparent 100%);
    mask-image: linear-gradient(180deg, transparent 0%, #000 30%, #000 70%, transparent 100%);
    opacity: .75;
  }

  .back-photo {
    position: absolute; inset: 0;
    background:
      radial-gradient(circle at 86% 33%, #3a3a3a 0, #242424 70px, transparent 110px),
      radial-gradient(ellipse at 35% 40%, #2e2e2e 0, #1c1c1c 60%, #141414 100%);
  }

  .name {
    position: absolute; left: 53px; top: 194px;
    font-size: 49px; letter-spacing: 12px; line-height: 1;
    color: var(--ink-light); font-weight: 400;
  }
  .roles {
    position: absolute; left: 53px; top: 246px;
    font-size: 23px; color: var(--ink-light);
  }
  .contacts {
    position: absolute; left: 53px; top: 308px;
    list-style: none; font-size: 22px; color: var(--ink-light); line-height: 28px;
  }
  .contacts li { display: flex; align-items: center; gap: 14px; }
  .contacts svg { width: 20px; height: 20px; flex: none; }
  .titles {
    position: absolute; right: 54px; top: 308px;
    font-size: 22px; color: var(--ink-light); line-height: 28px; text-align: right;
  }
  .colour-bar {
    position: absolute; left: 0; right: 0; bottom: 0; height: 5px; display: flex;
  }
  .colour-bar span { flex: 1; }
  .colour-bar .red { background: var(--red); }
  .colour-bar .yellow { background: var(--yellow); }
  .colour-bar .green { background: var(--green); }
  .colour-bar .purple { background: var(--purple); }
</style>
</head>
<body>
  <section class="card card--front">
    <div class="waveform" role="img" aria-label="Dotted audio waveform fading from red through yellow and green to blue"></div>
  </section>

  <section class="card card--back">
    <div class="back-photo" role="img" aria-label="Dark photograph of a mixing console with a microphone head on the right"></div>
    <h1 class="name">Corwin Pellath</h1>
    <p class="roles">Sound | FOH | Monitors | Systems | Corporate</p>
    <ul class="contacts">
      <li>
        <svg viewBox="0 0 20 20" aria-hidden="true"><rect x="5" y="1.5" width="10" height="17" rx="1.5" fill="none" stroke="#f2f2f2" stroke-width="2"/><rect x="8" y="14.5" width="4" height="1.5" fill="#f2f2f2"/></svg>
        +61 402 918 357
      </li>
      <li>
        <svg viewBox="0 0 20 20" aria-hidden="true"><rect x="1" y="4" width="18" height="12" fill="#f2f2f2"/><path d="M1 4 L10 11 L19 4 M1 16 L8 9.5 M19 16 L12 9.5" fill="none" stroke="#1a1a1a" stroke-width="1.5"/></svg>
        corwinpellath@mailvexo.net
      </li>
    </ul>
    <p class="titles">Digital Audio Mixing Specialist<br>Live Event Technical Professional</p>
    <div class="colour-bar"><span class="red"></span><span class="yellow"></span><span class="green"></span><span class="purple"></span></div>
  </section>
</body>
</html>
```